Hair Salon using organic products looking for AWSOME new menu's!!

We want different and fun incorporating our logo. We would love a folding or tri-folding menu. Any ideas would be welcome we like different. We are an quilmo salon in a little colonial town, but don't like the colonial feel. we would like menu's that would not cost an arm and a leg to print. And we could update as prices and services change without having to re-do the entire design.

Target Market(s)

upper class clients with an interest in using plant based products on their hair and skin

Industry/Entity Type

Hair And Beauty

Requirements
Must have
• Logo, area for contact information and ability to list all salon services
Nice to have
• just a really fun different look to set us aside from other salons. We like to be different

```html
<!DOCTYPE html>
<html lang="en">
<head>
<meta charset="utf-8">
<title>Lumen Salon — Service Menu</title>
<link href="https://fonts.googleapis.com/css2?family=Crimson+Text:ital,wght@0,400;0,700;1,400&family=Marcellus+SC&display=swap" rel="stylesheet">
<style>
  :root {
    --page-bg: #ececec;
    --gold-light: #f0dc78;
    --gold-mid: #d7b24c;
    --gold-deep: #a87a2c;
    --tab-gold: #e9d16c;
    --panel-bg: #ffffff;
    --paper: #fafafa;
    --stripe: #f0f0f0;
    --rule: #e8d27a;
    --ink: #7d5a1c;
    --ink-soft: #8a6a2c;
    --white: #ffffff;
  }
  * { box-sizing: border-box; margin: 0; padding: 0; }
  html, body { width: 1200px; height: 1000px; overflow: hidden; }
  body {
    background: var(--page-bg);
    font-family: "Crimson Text", Georgia, serif;
    color: var(--ink);
    position: relative;
  }

  .menu-card {
    position: absolute;
    left: 129px; top: 131px;
    width: 966px; height: 684px;
    background: linear-gradient(100deg, var(--gold-mid) 0%, var(--gold-light) 35%, var(--gold-mid) 65%, var(--gold-deep) 100%);
  }
  .menu-sheet {
    position: absolute;
    left: 31px; top: 29px;
    width: 905px; height: 625px;
    background-color: var(--paper);
    background-image: repeating-linear-gradient(180deg, var(--stripe) 0 8px, transparent 8px 18px);
  }

  .brand {
    position: absolute;
    left: 50px; top: 15px; width: 180px;
    text-align: center;
  }
  .brand-mark {
    width: 56px; height: 56px;
    margin: 7px auto 0;
    border-radius: 50%;
    background: var(--gold-mid);
  }
  .brand-name {
    margin-top: 12px;
    font-family: "Marcellus SC", Georgia, serif;
    font-size: 19px;
    line-height: 22px;
    letter-spacing: 3px;
    color: var(--gold-mid);
    white-space: nowrap;
  }

  .service-panel {
    position: absolute;
    background: var(--panel-bg);
    border: 1px solid var(--rule);
  }
  .panel-title {
    position: absolute;
    top: -11px; left: 50%;
    transform: translateX(-50%);
    background: var(--tab-gold);
    padding: 0 12px;
    height: 21px;
    line-height: 22px;
    font-family: "Marcellus SC", Georgia, serif;
    font-weight: 400;
    font-size: 15px;
    letter-spacing: 1.5px;
    color: var(--ink);
    white-space: nowrap;
  }
  .panel-hair-styling { left: 24px;  top: 137px; width: 245px; height: 448px; padding-top: 39px; }
  .panel-hair-styling .panel-title { width: 146px; text-align: center; }
  .panel-coloring     { left: 330px; top: 37px;  width: 245px; height: 235px; padding-top: 38px; }
  .panel-waxing       { left: 333px; top: 307px; width: 245px; height: 278px; padding-top: 20px; }
  .panel-makeup       { left: 628px; top: 35px;  width: 244px; height: 414px; padding-top: 20px; }
  .panel-makeup .panel-title { width: 126px; text-align: center; }

  .service-list { list-style: none; }
  .service {
    height: 66.4px;
    padding: 0 18px 0 12px;
    position: relative;
  }
  .service-line {
    display: flex;
    align-items: baseline;
    font-size: 13px;
    font-weight: 700;
    line-height: 18px;
  }
  .service-line::before {
    content: "";
    width: 5px; height: 5px;
    border-radius: 50%;
    background: var(--tab-gold);
    margin-right: 5px;
    align-self: center;
    flex: none;
  }
  .service-name { white-space: nowrap; }
  .leader {
    flex: 1;
    border-bottom: 1.5px dotted var(--ink-soft);
    margin: 0 1px 3px;
  }
  .price { font-weight: 400; font-size: 12.5px; }
  .price-tag {
    border: 1px solid var(--rule);
    padding: 0 3px;
    line-height: 14px;
  }
  .service-desc {
    margin-left: 42px;
    font-style: italic;
    font-size: 11px;
    line-height: 17px;
    color: var(--ink);
  }
  .panel-coloring .service-desc { margin-left: 45px; }

  .contact-box {
    position: absolute;
    left: 627px; top: 462px;
    width: 244px; height: 146px;
    background: var(--tab-gold);
    padding: 5px;
  }
  .contact-inner {
    height: 100%;
    border: 1px solid var(--white);
    text-align: center;
    padding-top: 8px;
    color: var(--white);
  }
  .contact-mark {
    width: 18px; height: 18px;
    margin: 0 auto 3px;
    border-radius: 50%;
    background: var(--gold-deep);
  }
  .contact-name {
    font-family: "Marcellus SC", Georgia, serif;
    font-size: 8px;
    letter-spacing: 1.5px;
    color: var(--ink);
  }
  .contact-text {
    font-style: italic;
    font-size: 9.5px;
    line-height: 12px;
    padding: 2px 10px 0;
  }
  .social-row {
    display: flex;
    justify-content: center;
    gap: 10px;
    margin-top: 10px;
  }
  .social-badge {
    width: 26px; height: 26px;
    border-radius: 6px;
    background: var(--white);
  }
</style>
</head>
<body>
  <main class="menu-card" role="img" aria-label="Gold border band with a repeating white fleur ornament pattern">
    <section class="menu-sheet">

      <header class="brand">
        <div class="brand-mark"></div>
        <div class="brand-name">LUMEN SALON</div>
      </header>

      <section class="service-panel panel-hair-styling">
        <h2 class="panel-title">HAIR STYLING</h2>
        <ul class="service-list">
          <li class="service"><div class="service-line"><span class="service-name">Bridal Up Style</span><span class="leader"></span><span class="price price-tag">$15</span></div><p class="service-desc">Lorem ipsum dolor sit, consectetuer adipiscing.</p></li>
          <li class="service"><div class="service-line"><span class="service-name">Blow Dry</span><span class="leader"></span><span class="price price-tag">$10</span></div><p class="service-desc">Lorem ipsum dolo r sit, consectetuer adipiscing</p></li>
          <li class="service"><div class="service-line"><span class="service-name">Up Style</span><span class="leader"></span><span class="price price-tag">$20</span></div><p class="service-desc">Lorem ipsum dolor sit, consectetuer adipiscing.</p></li>
          <li class="service"><div class="service-line"><span class="service-name">Night Style</span><span class="leader"></span><span class="price price-tag">$15</span></div><p class="service-desc">Lorem ipsum dolor sit, consectetuer adipiscing.</p></li>
          <li class="service"><div class="service-line"><span class="service-name">Super Dry</span><span class="leader"></span><span class="price price-tag">$10</span></div><p class="service-desc">Lorem ipsum dolo r sit, consectetuer adipiscing</p></li>
          <li class="service"><div class="service-line"><span class="service-name">Diva Style</span><span class="leader"></span><span class="price price-tag">$20</span></div><p class="service-desc">Lorem ipsum dolor sit, consectetuer adipiscing.</p></li>
        </ul>
      </section>

      <section class="service-panel panel-coloring">
        <h2 class="panel-title">HAIR COLORING</h2>
        <ul class="service-list">
          <li class="service"><div class="service-line"><span class="service-name">Single Process Color</span><span class="leader"></span><span class="price">$15</span></div><p class="service-desc">Lorem ipsum dolor sit, consectetuer adipiscing.</p></li>
          <li class="service"><div class="service-line"><span class="service-name">Full Highlight</span><span class="leader"></span><span class="price">$10</span></div><p class="service-desc">Lorem ipsum dolo r sit, consectetuer adipiscing</p></li>
          <li class="service"><div class="service-line"><span class="service-name">Partial Highlight</span><span class="leader"></span><span class="price">$20</span></div><p class="service-desc">Lorem ipsum dolor sit, consectetuer adipiscing.</p></li>
        </ul>
      </section>

      <section class="service-panel panel-waxing">
        <h2 class="panel-title">WAXING</h2>
        <ul class="service-list">
          <li class="service"><div class="service-line"><span class="service-name">Eyebrow</span><span class="leader"></span><span class="price">$15</span></div><p class="service-desc">Lorem ipsum dolor sit, consectetuer adipiscing.</p></li>
          <li class="service"><div class="service-line"><span class="service-name">Lip</span><span class="leader"></span><span class="price">$10</span></div><p class="service-desc">Lorem ipsum dolo r sit, consectetuer adipiscing</p></li>
          <li class="service"><div class="service-line"><span class="service-name">Chin</span><span class="leader"></span><span class="price">$20</span></div><p class="service-desc">Lorem ipsum dolor sit, consectetuer adipiscing.</p></li>
          <li class="service"><div class="service-line"><span class="service-name">Cheeks</span><span class="leader"></span><span class="price">$20</span></div><p class="service-desc">Lorem ipsum dolor sit, consectetuer adipiscing.</p></li>
        </ul>
      </section>

      <section class="service-panel panel-makeup">
        <h2 class="panel-title">MAKE-UP</h2>
        <ul class="service-list">
          <li class="service"><div class="service-line"><span class="service-name">Application</span><span class="leader"></span><span class="price">$25</span></div><p class="service-desc">Lorem ipsum dolor sit, consectetuer adipiscing.</p></li>
          <li class="service"><div class="service-line"><span class="service-name">Eye Application</span><span class="leader"></span><span class="price">$10</span></div><p class="service-desc">Lorem ipsum dolo r sit, consectetuer adipiscing</p></li>
          <li class="service"><div class="service-line"><span class="service-name">Bridal Make-Up</span><span class="leader"></span><span class="price">$20</span></div><p class="service-desc">Lorem ipsum dolor sit, consectetuer adipiscing.</p></li>
          <li class="service"><div class="service-line"><span class="service-name">Make-Up Consultation</span><span class="leader"></span><span class="price">$25</span></div><p class="service-desc">Lorem ipsum dolor sit, consectetuer adipiscing.</p></li>
          <li class="service"><div class="service-line"><span class="service-name">Individual Lashes</span><span class="leader"></span><span class="price">$10</span></div><p class="service-desc">Lorem ipsum dolo r sit, consectetuer adipiscing</p></li>
          <li class="service"><div class="service-line"><span class="service-name">Nigth Make-Up</span><span class="leader"></span><span class="price">$20</span></div><p class="service-desc">Lorem ipsum dolor sit, consectetuer adipiscing.</p></li>
        </ul>
      </section>

      <aside class="contact-box">
        <div class="contact-inner">
          <div class="contact-mark"></div>
          <div class="contact-name">LUMEN SALON</div>
          <p class="contact-text">Lorem ipsum dolor sit amet, consectetuer adipiscing elit, sed diam nonummy nibh euismod tincidunt ut laoreet dolore magna aliquam erat volutpat.</p>
          <div class="social-row">
            <span class="social-badge"></span>
            <span class="social-badge"></span>
            <span class="social-badge"></span>
            <span class="social-badge"></span>
          </div>
        </div>
      </aside>

    </section>
  </main>
</body>
</html>
```